Crumb Joy pastry business card design

I need a logo and a business card design for my baking business, "Crumb Joy". I daily bake French pastries from scratch using high quality ingredients and directly cater to local customers. My product is very authentic but sold at a casual setting . I'm looking for a simple, cute, stylish yet earthy design. Like this kind of feel:
http://clipvista.example/71946302
Target Market(s)
Metropolitan food conscious consumers in their 20-40s
Industry/Entity Type
Business
Requirements
Must have
- Soft pastel colors or other types of color schemes that would remind French pastries.
email: welovecrumbles@mailnest.example
twitter@bitemesf
www.crumbjoyla.example
Nice to have
Should not have
- pictures of pastries - sketches are ok.

```html
<!DOCTYPE html>
<html lang="en">
<head>
<meta charset="utf-8">
<title>Crumb Joy – Business Card</title>
<link rel="stylesheet" href="https://fonts.googleapis.com/css2?family=Jost:wght@300;400;600&display=swap">
<style>
  :root {
    --backdrop: #ece7df;
    --card-olive: #c3b46a;
    --ink-white: #ffffff;
    --photo-plum: #6e5a78;
    --photo-mauve: #a08a9c;
    --photo-cream: #e9dccb;
    --photo-peach: #d8a774;
    --card-shadow: rgba(60, 45, 30, 0.22);
  }
  * { margin: 0; padding: 0; box-sizing: border-box; }
  html, body { width: 1200px; height: 880px; overflow: hidden; }
  body {
    background: var(--backdrop);
    font-family: "Jost", "Futura", sans-serif;
    position: relative;
  }
  .card {
    position: absolute;
    width: 560px;
    height: 320px;
    border-radius: 4px;
    overflow: hidden;
    box-shadow: 0 10px 24px var(--card-shadow);
  }

  /* Front side */
  .card-front { left: 600px; top: 110px; }
  .front-photo {
    position: absolute; inset: 0;
    background:
      radial-gradient(ellipse at 78% 62%, var(--photo-cream) 0%, rgba(233,220,203,0) 55%),
      radial-gradient(ellipse at 14% 10%, var(--photo-peach) 0%, rgba(216,167,116,0) 35%),
      linear-gradient(160deg, var(--photo-plum) 0%, var(--photo-mauve) 50%, var(--photo-cream) 100%);
  }
  .front-logo {
    position: absolute;
    left: 0; right: 0; top: 100px;
    display: flex; justify-content: center; align-items: center; gap: 16px;
    color: var(--ink-white);
  }
  .brand-name {
    font-weight: 300;
    font-size: 58px;
    letter-spacing: 0.14em;
    line-height: 1;
  }
  .brand-dot {
    width: 14px; height: 14px;
    border-radius: 50%;
    background: var(--ink-white);
  }
  .front-url {
    position: absolute;
    left: 0; right: 0; top: 210px;
    text-align: center;
    color: var(--ink-white);
    font-weight: 300;
    font-size: 24px;
    letter-spacing: 0.08em;
  }
  .front-url strong { font-weight: 600; }

  /* Back side */
  .card-back { left: 40px; top: 450px; background: var(--card-olive); }
  .contact-list {
    list-style: none;
    position: absolute;
    left: 64px; top: 72px;
    color: var(--ink-white);
    font-weight: 400;
    font-size: 21px;
    letter-spacing: 0.07em;
  }
  .contact-item {
    display: flex; align-items: center; gap: 20px;
    height: 40px;
  }
  .contact-icon { width: 22px; height: 22px; flex: none; }
  .social-square {
    width: 18px; height: 18px; margin: 2px;
    background: var(--ink-white);
    border-radius: 3px;
  }
  .corner-ornament {
    position: absolute;
    right: 0; bottom: 0;
    width: 110px; height: 86px;
    background: var(--ink-white);
    border-top-left-radius: 60px 54px;
  }
</style>
</head>
<body>

  <section class="card card-front" aria-label="Card front">
    <div class="front-photo" role="img" aria-label="Soft-focus photo of a glass dish of toasted meringue tart in plum and cream tones"></div>
    <div class="front-logo">
      <span class="brand-name">CRUMB JOY</span>
      <span class="brand-dot"></span>
    </div>
    <p class="front-url">www.<strong>crumbjoyla</strong>.example</p>
  </section>

  <section class="card card-back" aria-label="Card back">
    <ul class="contact-list">
      <li class="contact-item">
        <svg class="contact-icon" viewBox="0 0 22 22" aria-hidden="true">
          <rect x="1" y="4" width="20" height="14" fill="none" stroke="#fff" stroke-width="1.6"/>
          <polyline points="1,4 11,12 21,4" fill="none" stroke="#fff" stroke-width="1.6"/>
        </svg>
        <span>welovecrumbles@mailnest.example</span>
      </li>
      <li class="contact-item">
        <span class="contact-icon social-square" aria-hidden="true"></span>
        <span>@crumbjoyla</span>
      </li>
      <li class="contact-item">
        <svg class="contact-icon" viewBox="0 0 22 22" aria-hidden="true">
          <circle cx="11" cy="11" r="9.5" fill="none" stroke="#fff" stroke-width="1.6"/>
          <ellipse cx="11" cy="11" rx="4.2" ry="9.5" fill="none" stroke="#fff" stroke-width="1.4"/>
          <line x1="1.5" y1="11" x2="20.5" y2="11" stroke="#fff" stroke-width="1.4"/>
          <line x1="3.5" y1="6" x2="18.5" y2="6" stroke="#fff" stroke-width="1.2"/>
          <line x1="3.5" y1="16" x2="18.5" y2="16" stroke="#fff" stroke-width="1.2"/>
        </svg>
        <span>www.crumbjoyla.example</span>
      </li>
    </ul>
    <div class="corner-ornament" role="img" aria-label="White scalloped cloud ornament in the card corner"></div>
  </section>

</body>
</html>
```